Infographic Design Improvements

Technically this is not a logo that we are looking for. More of a info-graphic. We have three segments of our company that we are proud of with their own capabilities and we are looking for improved graphics to illustrate the capabilities of each segment. I have attached the three info-graphics that we are looking to improve. They are all similar to each other. The name of the segments surrounded by the different responsibilities of each segment.

Target Market(s)

Someone who is buying plastic molding

Industry/Entity Type

Manufacturing

Logo Text

Halvard Tooling, Where Your Plans Find Form

Requirements
Must have
• Must have the words that we have selected
Nice to have
• Better graphics for the icons, would like based on current logo color. can add others as well, but the logo colors should be in there. Should match nicely with current logo. Logo has been included.

```html
<!DOCTYPE html>
<html lang="en">
<head>
<meta charset="utf-8">
<title>Halvard Tooling – Capabilities</title>
<link rel="stylesheet" href="https://fonts.googleapis.com/css2?family=Roboto:wght@500;700;900&display=swap">
<style>
  :root {
    --navy: #1b1f8f;
    --green: #3ea535;
    --green-light: #74c64f;
    --green-dark: #2e8a2a;
    --bg-top: #f1f1f1;
    --bg-bottom: #fbfbfb;
    --white: #ffffff;
  }
  html, body {
    margin: 0;
    padding: 0;
    width: 1200px;
    height: 2539px;
    overflow: hidden;
  }
  body {
    background: linear-gradient(180deg, var(--bg-top), var(--bg-bottom) 40%, var(--bg-top));
    font-family: "Roboto", Arial, sans-serif;
  }
  .capability-map { display: block; width: 1200px; height: 2539px; }
  .brand-name { font-weight: 900; font-size: 34px; fill: var(--navy); letter-spacing: -0.5px; }
  .brand-tagline { font-weight: 700; font-size: 9.5px; fill: var(--navy); letter-spacing: 0.3px; }
  .label { font-weight: 500; font-size: 14px; fill: var(--navy); }
  .hub-title { font-weight: 700; font-size: 14px; fill: var(--white); }
  .spoke-navy { stroke: var(--navy); stroke-width: 5; stroke-linecap: round; }
  .spoke-green { stroke: var(--green); stroke-width: 5; stroke-linecap: round; }
  .joint { fill: var(--green-light); }
  .icon { fill: var(--green); }
  .icon-dark { fill: var(--green-dark); }
  .icon-line { fill: none; stroke: var(--green); stroke-width: 4; stroke-linecap: round; stroke-linejoin: round; }
  .icon-white { fill: var(--white); }
  .icon-white-line { fill: none; stroke: var(--white); stroke-width: 3; stroke-linecap: round; stroke-linejoin: round; }
  .ring-outer { fill: var(--navy); }
  .ring-gap { fill: var(--white); }
  .ring-core { fill: url(#coreGradient); }
  .figure-slot { fill: var(--green); opacity: 0.85; }
</style>
</head>
<body>
<svg class="capability-map" viewBox="0 0 709 1500" xmlns="http://www.w3.org/2000/svg">
  <defs>
    <radialGradient id="coreGradient" cx="50%" cy="40%" r="60%">
      <stop offset="0" stop-color="#7fd157"/>
      <stop offset="1" stop-color="#329d2f"/>
    </radialGradient>
  </defs>

  <!-- Brand -->
  <g class="brand">
    <text class="brand-name" x="354" y="57" text-anchor="middle">HALVARD TOOLING</text>
    <text class="brand-tagline" x="354" y="76" text-anchor="middle">CUSTOM MOLDED PARTS, CONCEPT TO PRODUCTION</text>
  </g>

  <!-- ========== Idea Factory ========== -->
  <g class="hub hub-idea">
    <line class="spoke-navy" x1="298" y1="280" x2="232" y2="238"/>
    <line class="spoke-navy" x1="360" y1="270" x2="362" y2="192"/>
    <line class="spoke-navy" x1="418" y1="280" x2="480" y2="238"/>
    <line class="spoke-navy" x1="434" y1="333" x2="497" y2="330"/>
    <line class="spoke-navy" x1="420" y1="385" x2="470" y2="428"/>
    <line class="spoke-navy" x1="323" y1="398" x2="285" y2="455"/>
    <line class="spoke-navy" x1="277" y1="337" x2="222" y2="360"/>

    <circle class="ring-outer" cx="357" cy="338" r="72"/>
    <circle class="ring-gap" cx="357" cy="338" r="66"/>
    <circle class="ring-outer" cx="357" cy="338" r="63"/>
    <circle class="ring-core" cx="357" cy="338" r="59"/>

    <circle class="joint" cx="298" cy="280" r="5"/>
    <circle class="joint" cx="360" cy="268" r="5"/>
    <circle class="joint" cx="418" cy="282" r="5"/>
    <circle class="joint" cx="434" cy="333" r="5"/>
    <circle class="joint" cx="420" cy="385" r="5"/>
    <circle class="joint" cx="323" cy="398" r="5"/>
    <circle class="joint" cx="277" cy="337" r="5"/>

    <g class="core-icon">
      <path class="icon-white-line" d="M349 330 a10 10 0 1 1 16 0 c-3 4 -4 6 -4 9 h-8 c0 -3 -1 -5 -4 -9z"/>
      <line class="icon-white-line" x1="353" y1="344" x2="361" y2="344"/>
      <line class="icon-white-line" x1="340" y1="310" x2="344" y2="314"/>
      <line class="icon-white-line" x1="374" y1="310" x2="370" y2="314"/>
      <line class="icon-white-line" x1="357" y1="302" x2="357" y2="307"/>
    </g>
    <text class="hub-title" x="357" y="372" text-anchor="middle">Idea Factory</text>

    <!-- Ideation -->
    <g class="icon-bulb">
      <path class="icon" d="M190 212 a13 13 0 1 1 26 0 c0 6 -5 9 -6 14 h-14 c-1 -5 -6 -8 -6 -14z"/>
      <rect class="icon" x="196" y="229" width="14" height="4" rx="1"/>
      <rect class="icon" x="198" y="235" width="10" height="4" rx="1"/>
      <line class="icon-line" x1="203" y1="184" x2="203" y2="190"/>
      <line class="icon-line" x1="182" y1="193" x2="186" y2="197"/>
      <line class="icon-line" x1="224" y1="193" x2="220" y2="197"/>
      <line class="icon-line" x1="175" y1="212" x2="180" y2="212"/>
      <line class="icon-line" x1="226" y1="212" x2="231" y2="212"/>
    </g>
    <text class="label" x="199" y="266" text-anchor="middle">Ideation</text>

    <!-- Numerous Options -->
    <g class="icon-venn">
      <circle class="icon" cx="362" cy="162" r="27"/>
      <circle cx="355" cy="155" r="11" fill="none" stroke="#fff" stroke-width="1.5"/>
      <circle cx="369" cy="155" r="11" fill="none" stroke="#fff" stroke-width="1.5"/>
      <circle cx="362" cy="168" r="11" fill="none" stroke="#fff" stroke-width="1.5"/>
    </g>
    <text class="label" x="404" y="161">Numerous</text>
    <text class="label" x="413" y="177">Options</text>

    <!-- Cost Analysis -->
    <g class="icon-calculator">
      <rect class="icon" x="495" y="185" width="40" height="52" rx="3"/>
      <rect class="icon-white" x="501" y="191" width="28" height="9"/>
      <g class="icon-white">
        <rect x="503" y="205" width="6" height="6"/><rect x="512" y="205" width="6" height="6"/><rect x="521" y="205" width="6" height="6"/>
        <rect x="512" y="214" width="6" height="6"/><rect x="521" y="214" width="6" height="6"/>
        <rect x="512" y="223" width="6" height="6"/><rect x="521" y="223" width="6" height="6"/>
      </g>
      <circle class="icon" cx="498" cy="228" r="13" stroke="#fff" stroke-width="2"/>
      <text x="498" y="234" text-anchor="middle" fill="#fff" font-weight="700" font-size="16">$</text>
    </g>
    <text class="label" x="478" y="264">Cost Analysis</text>

    <!-- Tooling Plans -->
    <g class="icon-plans">
      <rect x="503" y="300" width="38" height="50" rx="3" fill="none" stroke="var(--green)" stroke-width="4"/>
      <line class="icon-line" x1="509" y1="294" x2="509" y2="302"/><line class="icon-line" x1="518" y1="294" x2="518" y2="302"/><line class="icon-line" x1="527" y1="294" x2="527" y2="302"/><line class="icon-line" x1="536" y1="294" x2="536" y2="302"/>
      <line class="icon-line" x1="510" y1="314" x2="530" y2="314"/><line class="icon-line" x1="510" y1="324" x2="526" y2="324"/><line class="icon-line" x1="510" y1="334" x2="522" y2="334"/>
      <path class="icon" d="M527 342 l22 -26 l7 6 l-22 26 l-9 3z"/>
    </g>
    <text class="label" x="485" y="375">Tooling Plans</text>

    <!-- Timeline -->
    <g class="icon-calendar">
      <rect class="icon" x="473" y="428" width="52" height="44" rx="4"/>
      <rect class="icon-white" x="478" y="440" width="42" height="27"/>
      <g class="icon"><rect x="483" y="445" width="6" height="5"/><rect x="492" y="445" width="6" height="5"/><rect x="501" y="445" width="6" height="5"/><rect x="483" y="454" width="6" height="5"/><rect x="492" y="454" width="6" height="5"/></g>
      <circle class="icon" cx="533" cy="477" r="16" stroke="#fff" stroke-width="2"/>
      <path class="icon-white-line" d="M533 467 v10 h8"/>
    </g>
    <text class="label" x="521" y="516" text-anchor="middle">Timeline</text>

    <!-- Product Requirements -->
    <g class="icon-checklist">
      <rect x="224" y="445" width="40" height="52" rx="3" fill="none" stroke="var(--green)" stroke-width="4"/>
      <rect class="icon" x="236" y="440" width="16" height="8" rx="2"/>
      <path class="icon-line" d="M230 461 l3 3 l5 -5 M243 462 h14 M230 474 l3 3 l5 -5 M243 475 h14 M230 487 l3 3 l5 -5 M243 488 h10"/>
      <circle class="icon" cx="271" cy="493" r="13" stroke="#fff" stroke-width="2"/>
      <path class="icon-white-line" d="M265 493 l4 4 l8 -8"/>
    </g>
    <text class="label" x="248" y="523" text-anchor="middle">Product Requirements</text>

    <!-- Program Support -->
    <rect class="figure-slot" x="132" y="322" width="80" height="62" rx="6" role="img" aria-label="Icon of three support team members joined together"/>
    <text class="label" x="171" y="407" text-anchor="middle">Program Support</text>
  </g>

  <!-- ========== Operations ========== -->
  <g class="hub hub-operations">
    <line class="spoke-green" x1="360" y1="718" x2="363" y2="645"/>
    <line class="spoke-green" x1="418" y1="745" x2="492" y2="693"/>
    <line class="spoke-green" x1="441" y1="800" x2="510" y2="797"/>
    <line class="spoke-green" x1="427" y1="857" x2="485" y2="905"/>
    <line class="spoke-green" x1="378" y1="876" x2="393" y2="918"/>
    <line class="spoke-green" x1="320" y1="870" x2="278" y2="918"/>
    <line class="spoke-green" x1="271" y1="802" x2="208" y2="828"/>
    <line class="spoke-green" x1="296" y1="744" x2="218" y2="690"/>

    <circle class="ring-outer" cx="357" cy="797" r="88"/>
    <circle class="ring-gap" cx="357" cy="797" r="81"/>
    <circle class="ring-outer" cx="357" cy="797" r="77"/>
    <circle class="ring-core" cx="357" cy="797" r="72"/>

    <circle class="joint" cx="360" cy="718" r="5"/>
    <circle class="joint" cx="418" cy="745" r="5"/>
    <circle class="joint" cx="441" cy="800" r="5"/>
    <circle class="joint" cx="427" cy="857" r="5"/>
    <circle class="joint" cx="378" cy="876" r="5"/>
    <circle class="joint" cx="320" cy="870" r="5"/>
    <circle class="joint" cx="271" cy="802" r="5"/>
    <circle class="joint" cx="296" cy="744" r="5"/>

    <g class="core-icon">
      <circle cx="366" cy="797" r="11" fill="none" stroke="#fff" stroke-width="6" stroke-dasharray="4 3"/>
      <circle class="icon-white" cx="366" cy="797" r="8"/>
      <circle class="ring-core" cx="366" cy="797" r="3.5"/>
      <circle cx="343" cy="796" r="7" fill="none" stroke="#fff" stroke-width="4" stroke-dasharray="3 2.5"/>
      <circle cx="351" cy="777" r="4" fill="none" stroke="#fff" stroke-width="3" stroke-dasharray="2 2"/>
      <path class="icon-white-line" d="M335 778 a28 28 0 0 1 38 -10"/>
      <path class="icon-white-line" d="M378 816 a28 28 0 0 1 -38 8"/>
    </g>
    <text class="hub-title" x="357" y="849" text-anchor="middle">Operations</text>

    <!-- Control -->
    <g class="icon-sliders">
      <line class="icon-line" x1="333" y1="593" x2="393" y2="593"/><circle cx="348" cy="593" r="6" fill="#fff" stroke="var(--green)" stroke-width="4"/>
      <line class="icon-line" x1="333" y1="611" x2="393" y2="611"/><circle cx="370" cy="611" r="6" fill="#fff" stroke="var(--green)" stroke-width="4"/>
      <line class="icon-line" x1="333" y1="630" x2="393" y2="630"/><circle cx="370" cy="630" r="6" fill="#fff" stroke="var(--green)" stroke-width="4"/>
    </g>
    <text class="label" x="404" y="613">Control</text>

    <!-- Oversee -->
    <g class="icon-magnifier">
      <circle cx="492" cy="652" r="17" fill="none" stroke="var(--green)" stroke-width="6"/>
      <line x1="505" y1="666" x2="523" y2="685" stroke="var(--green)" stroke-width="9" stroke-linecap="round"/>
    </g>
    <text class="label" x="529" y="660">Oversee</text>

    <!-- Cost -->
    <g class="icon-moneybag">
      <path class="icon" d="M541 745 h20 l-5 10 c18 8 28 22 28 36 c0 18 -14 28 -33 28 s-33 -10 -33 -28 c0 -14 10 -28 28 -36z"/>
      <text x="551" y="807" text-anchor="middle" fill="#fff" font-weight="700" font-size="30">$</text>
    </g>
    <text class="label" x="555" y="846" text-anchor="middle">Cost</text>

    <!-- Planning -->
    <rect class="figure-slot" x="485" y="900" width="92" height="72" rx="6" role="img" aria-label="Icon of two people planning at a table with speech bubbles"/>
    <text class="label" x="536" y="997" text-anchor="middle">Planning</text>

    <!-- Resources -->
    <g class="icon-globe">
      <circle cx="398" cy="955" r="33" fill="none" stroke="var(--green)" stroke-width="4"/>
      <ellipse cx="398" cy="955" rx="14" ry="33" fill="none" stroke="var(--green)" stroke-width="3"/>
      <line x1="398" y1="922" x2="398" y2="988" stroke="var(--green)" stroke-width="3"/>
      <line x1="365" y1="955" x2="431" y2="955" stroke="var(--green)" stroke-width="3"/>
      <path d="M370 938 h56 M370 972 h56" stroke="var(--green)" stroke-width="3"/>
    </g>
    <text class="label" x="400" y="1009" text-anchor="middle">Resources</text>

    <!-- Strategy -->
    <g class="icon-puzzle">
      <path class="icon" d="M195 905 h18 a6 6 0 1 1 10 0 h14 v16 a6 6 0 1 0 0 10 v14 h-16 a6 6 0 1 1 -10 0 h-16z"/>
      <path class="icon" d="M240 905 h24 v38 h-24 v-12 a6 6 0 1 0 0 -10z"/>
      <path class="icon" d="M186 948 h24 v10 a6 6 0 1 0 10 0 v-10 h12 v36 h-46z"/>
      <path class="icon" d="M240 975 l20 -20 l8 8 a6 6 0 1 1 8 8 l8 8 l-20 20 l-8 -8 a6 6 0 1 0 -8 -8z"/>
    </g>
    <text class="label" x="182" y="1002" text-anchor="middle">Strategy</text>

    <!-- Requirements -->
    <g class="icon-clipboard">
      <rect x="136" y="783" width="64" height="78" rx="4" fill="none" stroke="var(--green)" stroke-width="5"/>
      <rect class="icon" x="155" y="776" width="26" height="11" rx="2"/>
      <path class="icon-line" d="M146 803 l4 4 l7 -7 M164 804 h26 M146 820 l4 4 l7 -7 M164 821 h26 M146 837 l4 4 l7 -7 M164 838 h26 M146 852 l4 4 l7 -7 M164 853 h22"/>
    </g>
    <text class="label" x="167" y="883" text-anchor="middle">Requirements</text>

    <!-- Input Output -->
    <g class="icon-arrows">
      <path class="icon" d="M146 661 l18 -18 v10 h28 v16 h-28 v10z"/>
      <path class="icon" d="M212 685 l-18 -18 v10 h-42 v16 h42 v10z"/>
    </g>
    <text class="label" x="182" y="726" text-anchor="middle">Input Output</text>
  </g>

  <!-- ========== Technology Center ========== -->
  <g class="hub hub-technology">
    <line class="spoke-navy" x1="381" y1="1192" x2="402" y2="1150"/>
    <line class="spoke-navy" x1="420" y1="1228" x2="482" y2="1213"/>
    <line class="spoke-navy" x1="419" y1="1345" x2="455" y2="1378"/>
    <line class="spoke-navy" x1="316" y1="1323" x2="278" y2="1383"/>
    <line class="spoke-navy" x1="272" y1="1285" x2="218" y2="1305"/>
    <line class="spoke-navy" x1="282" y1="1222" x2="230" y2="1190"/>

    <circle class="ring-outer" cx="350" cy="1270" r="82"/>
    <circle class="ring-gap" cx="350" cy="1270" r="75"/>
    <circle class="ring-outer" cx="350" cy="1270" r="71"/>
    <circle class="ring-core" cx="350" cy="1270" r="66"/>

    <circle class="joint" cx="381" cy="1192" r="5"/>
    <circle class="joint" cx="420" cy="1228" r="5"/>
    <circle class="joint" cx="419" cy="1345" r="5"/>
    <circle class="joint" cx="316" cy="1323" r="5"/>
    <circle class="joint" cx="272" cy="1285" r="5"/>
    <circle class="joint" cx="282" cy="1222" r="5"/>

    <g class="core-icon">
      <ellipse cx="347" cy="1249" rx="30" ry="11" fill="none" stroke="#fff" stroke-width="3"/>
      <ellipse cx="347" cy="1249" rx="30" ry="11" fill="none" stroke="#fff" stroke-width="3" transform="rotate(60 347 1249)"/>
      <ellipse cx="347" cy="1249" rx="30" ry="11" fill="none" stroke="#fff" stroke-width="3" transform="rotate(-60 347 1249)"/>
      <circle class="icon-white" cx="347" cy="1249" r="6"/>
    </g>
    <text class="hub-title" x="350" y="1298" text-anchor="middle">Technology</text>
    <text class="hub-title" x="350" y="1313" text-anchor="middle">Center</text>

    <!-- Mold Building -->
    <g class="icon-tools">
      <path class="icon" d="M400 1102 a10 10 0 0 0 13 13 l26 26 l6 -6 l-26 -26 a10 10 0 0 0 -13 -13 l6 6 l-3 4 l-4 2z"/>
      <path class="icon" d="M436 1098 l10 10 l-28 28 l-4 10 l-12 6 l-3 -3 l6 -12 l10 -4z"/>
    </g>
    <text class="label" x="453" y="1128">Mold Building</text>

    <!-- Scientific Molding -->
    <g class="icon-mold">
      <rect x="496" y="1183" width="26" height="30" fill="none" stroke="var(--green)" stroke-width="4"/>
      <rect class="icon" x="522" y="1193" width="22" height="10"/>
      <rect x="544" y="1176" width="10" height="46" fill="none" stroke="var(--green)" stroke-width="4"/>
      <rect class="icon" x="558" y="1172" width="8" height="54"/>
      <path class="icon-line" d="M502 1192 h12 M502 1204 h12"/>
    </g>
    <text class="label" x="479" y="1255">Scientific Molding</text>

    <!-- Packaging -->
    <g class="icon-box">
      <path class="icon" d="M462 1374 L450 1360 L494 1344 L507 1356z"/>
      <path class="icon" d="M552 1374 L564 1360 L520 1344 L507 1356z"/>
      <path class="icon-dark" d="M462 1374 L507 1356 L552 1374 L507 1392z"/>
      <path class="icon" d="M462 1378 L505 1396 L505 1430 L462 1412z"/>
      <path class="icon" d="M552 1378 L509 1396 L509 1430 L552 1412z"/>
    </g>
    <text class="label" x="512" y="1451" text-anchor="middle">Packaging</text>

    <!-- Approval and Validation -->
    <g class="icon-approval">
      <rect x="222" y="1378" width="38" height="50" rx="3" fill="none" stroke="var(--green)" stroke-width="4"/>
      <rect x="230" y="1372" width="38" height="50" rx="3" fill="#fafafa" stroke="var(--green)" stroke-width="4"/>
      <path class="icon-line" d="M237 1386 h22 M237 1396 h22 M237 1406 h14"/>
      <circle class="icon" cx="268" cy="1418" r="14" stroke="#fff" stroke-width="2"/>
      <path class="icon-white-line" d="M261 1418 l5 5 l9 -9"/>
    </g>
    <text class="label" x="253" y="1453" text-anchor="middle">Approval and Validation</text>

    <!-- Automation -->
    <g class="icon-gears">
      <circle cx="170" cy="1300" r="26" fill="none" stroke="var(--green)" stroke-width="9" stroke-dasharray="16 4 0 26"/>
      <circle cx="170" cy="1300" r="15" fill="none" stroke="var(--green)" stroke-width="7" stroke-dasharray="6 3"/>
      <circle class="icon" cx="170" cy="1300" r="6"/>
      <circle cx="127" cy="1296" r="8" fill="none" stroke="var(--green)" stroke-width="5" stroke-dasharray="3 2"/>
      <circle cx="186" cy="1263" r="8" fill="none" stroke="var(--green)" stroke-width="5" stroke-dasharray="3 2"/>
      <circle cx="186" cy="1337" r="8" fill="none" stroke="var(--green)" stroke-width="5" stroke-dasharray="3 2"/>
    </g>
    <text class="label" x="153" y="1362" text-anchor="middle">Automation</text>

    <!-- Performance Test -->
    <rect class="figure-slot" x="145" y="1100" width="85" height="70" rx="6" role="img" aria-label="Icon of a person reviewing a timed test report"/>
    <text class="label" x="168" y="1205" text-anchor="middle">Performance Test</text>
  </g>
</svg>
</body>
</html>
```